Halvick Ledgers & Advisory Tri-Fold Brochure (8.5"x11")

I need a professional looking brochure for my bookkeeping business. I am looking for something professional yet casual (not too corporate looking). I have attached a sample brochure that will outline the areas and a copy of our logo. I'd like to stick with shades of blue. The final product should communicate professional and personal.

Target Market(s)

Small service businesses.

Industry/Entity Type

Business

Font styles to use
Sans Serif

Requirements
Must have
• Professional looking photos of people in areas where it asks for a picture.

```html
<!DOCTYPE html>
<html lang="en">
<head>
<meta charset="utf-8">
<title>Halvick Ledgers &amp; Advisory – Tri-Fold Brochure</title>
<link rel="stylesheet" href="https://fonts.googleapis.com/css2?family=Lato:wght@400;700&family=Libre+Baskerville:wght@400;700&display=swap">
<style>
  :root {
    --page-bg: #e4e6e9;
    --ink: #151515;
    --charcoal: #262626;
    --charcoal-light: #3a3a3a;
    --brand-blue: #1b8fd2;
    --brand-blue-deep: #0d68a8;
    --accent-cyan: #2aa9e1;
    --paper: #f4f5f6;
    --white: #ffffff;
    --serif: "Libre Baskerville", "Times New Roman", serif;
    --sans: "Lato", Arial, sans-serif;
  }
  * { box-sizing: border-box; margin: 0; padding: 0; }
  html, body { width: 1200px; height: 668px; overflow: hidden; background: var(--page-bg); }
  .canvas { position: relative; width: 1200px; height: 668px; }
  .brochure {
    position: absolute; left: 194px; top: 24px;
    width: 812px; height: 620px;
    box-shadow: 0 6px 22px rgba(0,0,0,.22);
    overflow: hidden; background: var(--paper);
    font-family: var(--sans);
  }
  .brochure-art { position: absolute; inset: 0; }
  .text { position: absolute; }

  /* Panel 1 – inside flap */
  .heading-small {
    font-family: var(--serif); font-weight: 700; font-size: 13px;
    color: var(--accent-cyan); letter-spacing: .5px;
    border-bottom: 2px solid var(--accent-cyan); padding-bottom: 2px;
    display: inline-block;
  }
  .what-we-do { left: 21px; top: 18px; }
  .intro-copy {
    left: 21px; top: 44px; width: 240px;
    font-size: 9.6px; line-height: 1.32; color: var(--white);
  }
  .lets-talk { left: 21px; top: 183px; }
  .consult-note { left: 21px; top: 213px; font-size: 9.6px; color: var(--white); }
  .qualities { left: 21px; top: 230px; list-style: none; }
  .qualities li {
    display: flex; align-items: center; gap: 7px;
    font-size: 10px; font-weight: 700; color: var(--white);
    height: 22px;
  }

  /* Panel 2 – back */
  .contact-title {
    left: 305px; top: 90px;
    font-family: var(--serif); font-weight: 700; font-size: 17px; color: var(--ink);
    border-bottom: 2px solid var(--ink); padding-bottom: 2px;
  }
  .contact-line {
    display: flex; align-items: center; gap: 10px;
    font-size: 14px; font-weight: 700; color: var(--white);
  }
  .contact-phone { left: 305px; top: 124px; }
  .contact-email { left: 305px; top: 152px; }
  .slogan-lead { left: 305px; top: 362px; font-size: 14px; color: var(--ink); }
  .slogan-main {
    left: 305px; top: 380px;
    font-family: var(--serif); font-size: 22px; color: var(--brand-blue);
  }
  .brand-mark {
    display: flex; align-items: center; gap: 8px;
    font-family: var(--serif); font-weight: 400; color: var(--brand-blue);
  }
  .brand-mark .mark-square { background: var(--brand-blue); }
  .brand-back { left: 272px; width: 272px; top: 470px; justify-content: center; font-size: 30px; }
  .brand-back .mark-square { width: 20px; height: 20px; }
  .web-pill {
    position: absolute; height: 38px; bottom: 0;
    border-radius: 12px 12px 0 0;
    display: flex; align-items: center; justify-content: center;
    font-size: 13px; font-weight: 700; color: var(--white);
  }
  .web-pill-back { left: 302px; width: 215px; background: var(--brand-blue-deep); }
  .web-pill-cover { left: 572px; width: 214px; background: var(--charcoal); }

  /* Panel 3 – cover */
  .brand-cover { left: 544px; width: 268px; top: 52px; justify-content: center; font-size: 36px; }
  .brand-cover .mark-square { width: 24px; height: 24px; }
  .cover-title {
    left: 571px; top: 458px; font-family: var(--serif); color: var(--ink);
    line-height: 1.15;
  }
  .cover-title .big { display: block; font-size: 27px; }
  .cover-title .sub { display: block; font-size: 16.5px; }
</style>
</head>
<body>
<div class="canvas">
  <div class="brochure">
    <svg class="brochure-art" width="812" height="620" viewBox="0 0 812 620">
      <defs>
        <clipPath id="upper-region">
          <path d="M0,0 H812 V142 C540,212 270,282 0,344 Z"/>
        </clipPath>
        <clipPath id="lower-region">
          <path d="M0,344 C270,282 540,212 812,142 V620 H0 Z"/>
        </clipPath>
        <linearGradient id="charcoal-fill" x1="0" y1="0" x2="0" y2="1">
          <stop offset="0" stop-color="#1f1f1f"/>
          <stop offset="1" stop-color="#3a3a3a"/>
        </linearGradient>
        <linearGradient id="blue-fill" x1="0" y1="0" x2="1" y2="1">
          <stop offset="0" stop-color="#2aa5e4"/>
          <stop offset="1" stop-color="#0d68a8"/>
        </linearGradient>
        <linearGradient id="cover-top-fill" x1="0" y1="0" x2="0" y2="1">
          <stop offset="0" stop-color="#ffffff"/>
          <stop offset="1" stop-color="#e6e8ea"/>
        </linearGradient>
        <linearGradient id="finance-photo-fill" x1="0" y1="0" x2="1" y2="1">
          <stop offset="0" stop-color="#cfe3f3"/>
          <stop offset="1" stop-color="#6fb3e0"/>
        </linearGradient>
        <linearGradient id="team-photo-fill" x1="0" y1="0" x2="1" y2="1">
          <stop offset="0" stop-color="#d9dde2"/>
          <stop offset="1" stop-color="#6d7680"/>
        </linearGradient>
        <linearGradient id="back-lower-fill" x1="0" y1="0" x2="0" y2="1">
          <stop offset="0" stop-color="#f3f4f5"/>
          <stop offset="1" stop-color="#e3e5e8"/>
        </linearGradient>
      </defs>

      <g clip-path="url(#upper-region)">
        <rect x="0" y="0" width="272" height="360" fill="url(#charcoal-fill)"/>
        <rect x="272" y="0" width="272" height="360" fill="url(#blue-fill)"/>
        <rect x="544" y="0" width="268" height="360" fill="url(#cover-top-fill)"/>
      </g>

      <g clip-path="url(#lower-region)">
        <rect x="0" y="0" width="272" height="620" fill="url(#finance-photo-fill)"
              role="img" aria-label="Photo of a hand with a pen over financial charts, a calculator and glasses"/>
        <rect x="272" y="0" width="272" height="620" fill="url(#back-lower-fill)"/>
        <rect x="544" y="0" width="268" height="620" fill="url(#team-photo-fill)"
              role="img" aria-label="Photo of two smiling colleagues working together at a computer"/>
      </g>

      <path d="M544,404 C640,392 730,385 812,376 V620 H544 Z" fill="url(#blue-fill)"/>
      <path d="M544,404 C640,392 730,385 812,376" fill="none" stroke="var(--charcoal)" stroke-width="5"/>

      <path d="M0,350 C270,288 540,218 812,148" fill="none" stroke="#111" stroke-width="12"/>
      <path d="M0,338 C270,276 540,206 812,136" fill="none" stroke="var(--brand-blue)" stroke-width="5"/>
    </svg>

    <!-- Panel 1 -->
    <h2 class="text heading-small what-we-do">WHAT WE DO</h2>
    <p class="text intro-copy">Allow business owners to spend more time focusing on their core business by providing comprehensive bookkeeping and business consulting services. We provide the financial data and tools that allow businesses to maximize profitability and focus on growth and other areas of their business. We consider our business to be an extension of your business and look forward to the opportunity to exceed your expectations!</p>
    <h2 class="text heading-small lets-talk">LET'S TALK</h2>
    <p class="text consult-note">Schedule a no-obligation consultation today</p>
    <ul class="text qualities">
      <li><svg width="11" height="9" viewBox="0 0 11 9"><path d="M1,4.5 L4,7.5 L10,1" fill="none" stroke="var(--accent-cyan)" stroke-width="2"/></svg>TRUSTWORTHY</li>
      <li><svg width="11" height="9" viewBox="0 0 11 9"><path d="M1,4.5 L4,7.5 L10,1" fill="none" stroke="var(--accent-cyan)" stroke-width="2"/></svg>EXPERIENCED</li>
      <li><svg width="11" height="9" viewBox="0 0 11 9"><path d="M1,4.5 L4,7.5 L10,1" fill="none" stroke="var(--accent-cyan)" stroke-width="2"/></svg>RELIABLE</li>
    </ul>

    <!-- Panel 2 -->
    <h2 class="text contact-title">CONTACT US</h2>
    <p class="text contact-line contact-phone">
      <svg width="12" height="12" viewBox="0 0 24 24"><path d="M6.6 10.8a15.1 15.1 0 0 0 6.6 6.6l2.2-2.2a1 1 0 0 1 1-.25 11.4 11.4 0 0 0 3.6.57 1 1 0 0 1 1 1V20a1 1 0 0 1-1 1A17 17 0 0 1 3 4a1 1 0 0 1 1-1h3.5a1 1 0 0 1 1 1c0 1.25.2 2.45.57 3.57a1 1 0 0 1-.25 1z" fill="var(--ink)"/></svg>
      610.555.0142
    </p>
    <p class="text contact-line contact-email">
      <svg width="12" height="10" viewBox="0 0 12 10"><rect x="0" y="0" width="12" height="10" rx="1" fill="var(--ink)"/><path d="M0.5,1 L6,5.5 L11.5,1" fill="none" stroke="#6fb8e6" stroke-width="1"/></svg>
      dana@halvickledgers.com
    </p>
    <p class="text slogan-lead">IT'S NOT JUST MY BUSINESS</p>
    <p class="text slogan-main">IT'S MY NAME</p>
    <div class="text brand-mark brand-back"><span class="mark-square"></span>HL&amp;A</div>
    <div class="web-pill web-pill-back">www.halvickledgers.com</div>

    <!-- Panel 3 -->
    <div class="text brand-mark brand-cover"><span class="mark-square"></span>HL&amp;A</div>
    <h1 class="text cover-title">
      <span class="big">EXPERT</span>
      <span class="sub">BOOKKEEPING SERVICES</span>
      <span class="sub">FOR SMALL BUSINESS</span>
    </h1>
    <div class="web-pill web-pill-cover">www.halvickledgers.com</div>
  </div>
</div>
</body>
</html>
```